Brisk Lantern Accounting - New client package

I need a stationary package (presentation folder cover, welcome letter template/design, sample financial report template/design, business card and new logo) for my accounting business. I would like to see designs that use the color blue. Financial icons can be included in the design. The final design should be clean and communicate professionalism and the use of modern; user-friendly technology. Attached postcard files should help with overall design concept.

```html
<!DOCTYPE html>
<html lang="en">
<head>
<meta charset="utf-8">
<title>Brisk Lantern Accounting – Presentation Folder</title>
<link href="https://fonts.googleapis.com/css2?family=Montserrat:wght@400;500&display=swap" rel="stylesheet">
<style>
  :root {
    --backdrop: #d9dadc;
    --paper: #ffffff;
    --navy: #024f8f;
    --sky: #1595cc;
    --sky-veil: #6ab9e2;
    --photo-light: #b9d6ea;
    --photo-dark: #3f78ad;
    --hatch-grey: #e7e8ea;
    --ink-brand: #0b4f8f;
    --ink-light: #ffffff;
  }
  * { margin: 0; padding: 0; box-sizing: border-box; }
  html, body {
    width: 1200px; height: 854px; overflow: hidden;
    background: var(--backdrop);
    font-family: "Montserrat", sans-serif;
  }
  .folder-spread {
    position: absolute; left: 100px; top: 97px;
    width: 1000px; height: 660px;
    box-shadow: 0 18px 40px rgba(0,0,0,.18);
  }
  .folder-art { position: absolute; inset: 0; display: block; }

  .brand-name {
    position: absolute; display: flex; align-items: center; gap: 10px;
    text-transform: uppercase; font-weight: 500; letter-spacing: .06em; line-height: 1.1;
  }
  .brand-mark { flex: none; }

  .back-cover-brand { left: 56px; top: 520px; color: var(--ink-light); font-size: 11px; }
  .back-cover-brand .brand-mark { width: 14px; height: 14px; background: var(--ink-light); }

  .back-cover-contact {
    position: absolute; left: 56px; top: 566px;
    color: var(--ink-light); font-size: 8.5px; line-height: 1.45; font-weight: 400;
  }
  .contact-address { margin-bottom: 8px; }
  .contact-line { display: flex; align-items: center; gap: 6px; }
  .contact-line svg { width: 8px; height: 8px; flex: none; }

  .front-cover-brand { left: 735px; top: 458px; color: var(--ink-brand); font-size: 17px; }
  .front-cover-brand .brand-mark { width: 24px; height: 24px; background: var(--ink-brand); }
</style>
</head>
<body>
<main class="folder-spread">
  <svg class="folder-art" viewBox="0 0 1000 660" xmlns="http://www.w3.org/2000/svg">
    <defs>
      <linearGradient id="cityPhoto" x1="0" y1="1" x2="1" y2="0">
        <stop offset="0" stop-color="var(--photo-dark)"/>
        <stop offset=".5" stop-color="var(--photo-light)"/>
        <stop offset="1" stop-color="var(--photo-dark)"/>
      </linearGradient>
    </defs>
    <!-- paper -->
    <rect class="panel-back" x="0" y="0" width="500" height="660" fill="var(--paper)"/>
    <rect class="panel-front" x="500" y="0" width="500" height="660" fill="var(--paper)"/>
    <!-- back cover navy band -->
    <path class="band-navy" d="M0,105 C180,102 360,88 500,68 L500,660 L0,660 Z" fill="var(--navy)"/>
    <!-- front cover navy wedge -->
    <path class="wedge-navy" d="M500,95 L860,88 L555,660 L500,660 Z" fill="var(--navy)"/>
    <!-- front cover light area -->
    <path class="front-shade" role="img" aria-label="Fine diagonal line texture in light grey"
          d="M882,0 L1000,0 L1000,370 L712,392 Z" fill="var(--hatch-grey)"/>
    <!-- city photograph strip -->
    <path class="city-photo" role="img" aria-label="Photograph looking up at blue glass office towers against the sky"
          d="M0,345 L500,252 L945,238 L918,332 L500,348 L0,442 Z" fill="url(#cityPhoto)"/>
    <!-- translucent sky stripe -->
    <path class="stripe-veil" d="M0,442 L500,348 L690,342 L680,365 L500,372 L0,472 Z"
          fill="var(--sky-veil)" opacity=".85"/>
    <!-- sky blue lower field -->
    <path class="band-sky" d="M0,472 L500,372 L680,365 L555,660 L0,660 Z" fill="var(--sky)"/>
    <!-- spine -->
    <line x1="500" y1="0" x2="500" y2="660" stroke="rgba(0,0,0,.08)" stroke-width="1"/>
  </svg>

  <div class="brand-name back-cover-brand">
    <span class="brand-mark"></span>
    <span>Brisk Lantern<br>Accounting</span>
  </div>

  <address class="back-cover-contact" style="font-style:normal">
    <p class="contact-address">Level 12, Harbour Point Tower<br>18 Wattle Lane, Sydney</p>
    <p class="contact-line">
      <svg viewBox="0 0 10 10"><path d="M2,0 L4,0 L4.5,2.5 L3.2,3.4 C3.8,4.9 5.1,6.2 6.6,6.8 L7.5,5.5 L10,6 L10,8 C10,9 9,10 8,10 C3.6,10 0,6.4 0,2 C0,1 1,0 2,0 Z" fill="#fff"/></svg>
      555-210-4470
    </p>
    <p class="contact-line">
      <svg viewBox="0 0 10 10"><rect x="0.5" y="2" width="9" height="6" fill="none" stroke="#fff"/><path d="M0.5,2 L5,5.5 L9.5,2" fill="none" stroke="#fff"/></svg>
      info@brisklantern.com
    </p>
    <p class="contact-line">
      <svg viewBox="0 0 10 10"><circle cx="5" cy="5" r="4.5" fill="none" stroke="#fff"/><ellipse cx="5" cy="5" rx="2" ry="4.5" fill="none" stroke="#fff"/><line x1="0.5" y1="5" x2="9.5" y2="5" stroke="#fff"/></svg>
      www.brisklantern.com
    </p>
  </address>

  <div class="brand-name front-cover-brand">
    <span class="brand-mark"></span>
    <span>Brisk Lantern<br>Accounting</span>
  </div>
</main>
</body>
</html>
```